Professional website for psychological services

Create a professional, easy to navigate website using soothing coastal images and incorporate company logo in design. Website is for a small private clinic that provides psychological services and must be appealing to professional men and women. A website I really like is www.velmorlodge.example I would love something like similar.

Target Market(s)

Professional men and women seeking psychological services

Industry/Entity Type

Mental Health

Number of Pages Required

5+ page

Requirements
Must have
• The website must incorporate the logo provided. The name of the company/website is Brindle Oak Wellness Aftercare. Colors must compliment the logo, must be coastal and soothing yet very professional. I would like a website like www.velmorlodge.example
• Pages will be:Home, Services, FAQ and Contact Us. The images included of the building and office are for the contact us page. Under the tab Servies: Individual Psychotherapy, Family Therapy, EMDR I will provide specific content for each.
Nice to have
• I want the website to be easy to navigate and the font easy to read. The writing on the logo is very light and I'm open to changing it slightly if it will be better aesthetically.
Should not have
• Please no pictures of any swimsuits, alcoholic beverages, etc. This is a professional psychological clinic.

```html
<!DOCTYPE html>
<html lang="en">
<head>
<meta charset="utf-8">
<title>Brindle Oak Wellness Aftercare — Home</title>
<link href="https://fonts.googleapis.com/css2?family=Open+Sans:wght@400;600&family=Great+Vibes&family=Arimo:wght@400&display=swap" rel="stylesheet">
<style>
  :root{
    --backdrop:#d7dcdc;
    --page:#ffffff;
    --aqua:#1fb8d6;
    --ink:#111111;
    --nav-ink:#2a2a2a;
    --hero-sea:#2f5a60;
    --hero-deep:#23464c;
    --hero-sand:#7a5a4a;
    --white:#ffffff;
  }
  *{box-sizing:border-box;margin:0;padding:0}
  html,body{width:1200px;height:1200px;overflow:hidden;background:var(--backdrop)}
  body{position:relative;font-family:"Arimo",Arial,sans-serif}
  .page{position:absolute;left:69px;top:47px;width:1062px;height:1153px;background:var(--page);overflow:hidden}

  .site-header{position:absolute;left:0;top:0;width:100%;height:230px}
  .brand{position:absolute;top:92px;left:0;width:100%;display:flex;justify-content:center;align-items:center;gap:12px}
  .brand-dot{width:16px;height:16px;border-radius:50%;background:var(--aqua)}
  .brand-name{font-family:"Arimo",Arial,sans-serif;font-size:28px;color:var(--aqua);font-weight:400}
  .main-nav{position:absolute;top:188px;left:0;width:100%}
  .main-nav a{position:absolute;transform:translateX(-50%);font-size:14.5px;color:var(--nav-ink);text-decoration:none;white-space:nowrap}
  .main-nav a.is-active{color:var(--aqua)}

  .hero{position:absolute;left:0;top:230px;width:100%;height:423px;
    background:linear-gradient(160deg,#4a6a6c 0%,var(--hero-sea) 35%,var(--hero-deep) 65%,var(--hero-sand) 100%)}
  .hero-portrait{position:absolute;left:57px;top:51px;width:264px;height:264px;border-radius:50%;
    border:5px solid var(--aqua);background:radial-gradient(circle at 50% 45%,#8a6a58 0%,#4c6a3a 70%,#355a2c 100%)}
  .hero-quote{position:absolute;left:364px;top:120px;width:330px;color:var(--white);font-size:21px;line-height:25px}
  .hero-author{position:absolute;right:376px;top:200px;font-family:"Great Vibes",cursive;font-size:34px;color:var(--white)}
  .gallery-arrows{position:absolute;left:709px;top:64px}
  .gallery-main{position:absolute;left:713px;top:94px;width:216px;height:206px;background:linear-gradient(180deg,#d9cfbf,#8a5a40)}
  .gallery-next{position:absolute;left:938px;top:94px;width:124px;height:206px;background:linear-gradient(180deg,#b9c9cf,#5f7a4e)}
  .thumbs{position:absolute;top:316px;left:0}
  .thumb{position:absolute;top:0;width:59px;height:58px}
  .thumb.is-current{outline:2px solid var(--aqua)}
  .down-arrow{position:absolute;left:516px;top:340px}

  .about{position:absolute;left:0;top:653px;width:100%;height:408px;text-align:center}
  .about h2{position:absolute;top:82px;width:100%;font-family:"Arimo",Arial,sans-serif;font-weight:400;font-size:35px;color:var(--ink)}
  .about p{position:absolute;top:155px;left:166px;width:730px;font-family:"Open Sans",Arial,sans-serif;font-size:17px;line-height:35px;color:var(--ink)}
  .btn{position:absolute;top:284px;width:150px;height:50px;border-radius:9px;font-size:17px;display:flex;align-items:center;justify-content:center;text-decoration:none}
  .btn-primary{left:359px;background:var(--aqua);color:var(--white)}
  .btn-outline{left:554px;border:2px solid var(--aqua);color:var(--aqua);background:var(--white)}

  .band{position:absolute;left:0;top:1061px;width:100%;height:92px;background:linear-gradient(180deg,#3d5c60,#2c4d52)}
</style>
</head>
<body>
<div class="page">
  <header class="site-header">
    <div class="brand"><span class="brand-dot"></span><span class="brand-name">Brindle Oak Wellness Aftercare</span></div>
    <nav class="main-nav">
      <a class="is-active" href="#" style="left:390px">Home</a>
      <a href="#" style="left:475px">Services</a>
      <a href="#" style="left:558px">FAQ</a>
      <a href="#" style="left:646px">Contact Us</a>
    </nav>
  </header>

  <section class="hero" role="img" aria-label="Calm coastal bay with hills at dusk">
    <div class="hero-portrait" role="img" aria-label="Portrait photo of the clinician"></div>
    <p class="hero-quote">"Lorem ipsum dolor sit amet, consectetur adipiscing elit, sed do eiusmod tempor incididunt ut"</p>
    <p class="hero-author">Author's Name</p>
    <svg class="gallery-arrows" width="70" height="22" viewBox="0 0 70 22">
      <polyline points="14,3 6,11 14,19" fill="none" stroke="#1fb8d6" stroke-width="3.5"/>
      <polyline points="52,3 60,11 52,19" fill="none" stroke="#1fb8d6" stroke-width="3.5"/>
    </svg>
    <div class="gallery-main" role="img" aria-label="Photo of the clinic office interior"></div>
    <div class="gallery-next" role="img" aria-label="Photo of the clinic building with palm trees"></div>
    <div class="thumbs">
      <div class="thumb is-current" style="left:711px;background:#9a7a60" role="img" aria-label="Office thumbnail"></div>
      <div class="thumb" style="left:786px;background:#7f8f78" role="img" aria-label="Building thumbnail"></div>
      <div class="thumb" style="left:858px;background:linear-gradient(180deg,#2f6bb0,#20a0b8)" role="img" aria-label="Coastline thumbnail"></div>
      <div class="thumb" style="left:931px;background:linear-gradient(180deg,#c9c0a8,#8a8a70)" role="img" aria-label="Lakeside thumbnail"></div>
      <div class="thumb" style="left:1004px;background:linear-gradient(90deg,#e9ddd2,#8a5a3a)" role="img" aria-label="Sunset silhouette thumbnail"></div>
    </div>
    <svg class="down-arrow" width="30" height="36" viewBox="0 0 30 36">
      <line x1="15" y1="2" x2="15" y2="33" stroke="#fff" stroke-width="2.5"/>
      <polyline points="3,21 15,33 27,21" fill="none" stroke="#fff" stroke-width="2.5"/>
    </svg>
  </section>

  <section class="about">
    <h2>ABOUT BRINDLE OAK</h2>
    <p>Lorem ipsum dolor sit amet, consectetur adipiscing elit, sed do eiusmod tempor incididunt ut labore et dolore magna aliqua. Ut enim ad minim veniam, quis nostrud exercitation ullamco laboris nisi ut aliquip ex ea commodo consequat. Duis aute irure.</p>
    <a class="btn btn-primary" href="#">CONTACT US</a>
    <a class="btn btn-outline" href="#">LEARN MORE</a>
  </section>

  <div class="band" role="img" aria-label="Coastal bay with hills"></div>
</div>
</body>
</html>
```